Oregon Pawnbroker About Us Brochure

We need to make a front/back tri-fold "about us" informative brochure using the bullet points uploaded. Our association represents licensed pawnbrokers in the state of Oregon and this will be distributed to the entire legislative body in our state. I have attached our logo, but feel free to be creative with logo to enhance the overall appearance of the brochure.

Target Market(s)

Regulators and Politicians

Industry/Entity Type

Pawnbroker

Requirements
Must have
• Professional Appearance
Nice to have
• Graphics, color scheme

```html
<!DOCTYPE html>
<html lang="en">
<head>
<meta charset="utf-8">
<title>Willamette Pawnbrokers Guild – Tri-fold Brochure</title>
<link href="https://fonts.googleapis.com/css2?family=Montserrat:wght@400;500;600;700;800&family=Oswald:wght@500;600&display=swap" rel="stylesheet">
<style>
:root{
  --orange:#f0620f;
  --orange-deep:#e2520a;
  --orange-light:#f7893b;
  --ink:#2a2a2a;
  --navy:#1f2a44;
  --grey-card:#e4e4e4;
  --stage:#bdbdbd;
  --white:#ffffff;
}
*{box-sizing:border-box;margin:0;padding:0}
html,body{width:1200px;height:2296px;overflow:hidden}
body{background:var(--stage);font-family:"Montserrat",sans-serif;color:var(--ink);position:relative}
.spread{position:absolute;left:50px;width:1100px;height:855px;display:grid;grid-template-columns:repeat(3,1fr);background:var(--white);box-shadow:0 6px 18px rgba(0,0,0,.18);overflow:hidden}
.spread--inside{top:179px}
.spread--outside{top:1213px}
.panel{position:relative;overflow:hidden}
.panel--orange{background:linear-gradient(160deg,var(--orange-light) 0%,var(--orange) 45%,var(--orange-deep) 100%);color:var(--white)}
.photo{position:absolute;left:0;width:100%}
.section-title{font-weight:800;font-size:15px;letter-spacing:.2px;text-transform:uppercase;line-height:1.2}
.section-title em{font-style:normal;color:var(--orange)}
.rule{height:2px;background:#ccc;position:relative;margin-top:7px}
.rule::before{content:"";position:absolute;left:18px;top:-1px;width:26px;height:4px;background:var(--orange)}
.panel--orange .rule{background:rgba(255,255,255,.7)}
.panel--orange .rule::before{background:var(--white)}
.icon-row{display:flex;align-items:center;gap:22px;font-size:10px;line-height:1.25}
.icon-tile{flex:none;width:46px;height:46px;border-radius:8px;background:var(--orange);display:flex;align-items:center;justify-content:center;box-shadow:0 2px 4px rgba(0,0,0,.2)}
.icon-tile svg{width:26px;height:26px}

/* inside spread – panel 1 */
.industry__photo{top:0;height:200px;background:linear-gradient(180deg,#b9a592 0%,#d8cbbd 55%,#f3efea 100%)}
.industry__body{position:absolute;top:218px;left:38px;right:70px;z-index:1}
.industry__list{margin-top:22px;display:flex;flex-direction:column;gap:27px}
.industry__chess{bottom:0;height:130px;background:linear-gradient(180deg,rgba(255,255,255,0) 0%,#cfcfcf 45%,#7d7570 100%)}

/* inside spread – panel 2 */
.why{position:absolute;top:38px;left:38px;right:38px}
.why .section-title{font-size:14px}
.why .section-title .dark{color:var(--navy)}
.bullets{list-style:none;margin-top:20px;display:flex;flex-direction:column;gap:14px}
.bullets li{display:flex;gap:22px;font-size:10.5px;font-weight:500;line-height:1.25}
.bullets .dot{flex:none;width:14px;height:14px;border-radius:50%;background:var(--white);margin-top:2px}
.stats{margin-top:22px}
.stats__list{list-style:none;margin-top:20px;display:flex;flex-direction:column;gap:16px}
.stats__list li{display:flex;align-items:center;gap:20px;font-size:10.5px;font-weight:700;text-transform:uppercase;line-height:1.25}
.dollar{flex:none;width:20px;height:20px;border-radius:50%;background:var(--white);color:var(--orange);font-size:12px;font-weight:800;display:flex;align-items:center;justify-content:center}
.why__art{position:absolute;left:50px;right:40px;bottom:24px;height:150px;border-radius:6px;background:linear-gradient(135deg,#f9b233 0%,#f58a1f 50%,#2f5f9a 100%);opacity:.85}

/* inside spread – panel 3 */
.regulation{position:absolute;top:38px;left:28px;right:30px;z-index:1}
.reg__list{list-style:none;margin-top:22px;display:flex;flex-direction:column;gap:18px}
.reg__list li{display:flex;align-items:center;gap:20px;font-size:10px;line-height:1.25}
.reg__icon{flex:none;width:26px;height:26px;border-radius:50%;border:2px solid var(--orange);display:flex;align-items:center;justify-content:center}
.reg__icon span{width:12px;height:12px;border-radius:3px;background:var(--orange)}
.agencies{list-style:none;margin:22px 0 0 38px;display:flex;flex-direction:column;gap:13px}
.agencies li{display:flex;align-items:flex-start;gap:14px;font-size:9.5px;font-weight:700;text-transform:uppercase;line-height:1.25}
.agencies .mark{flex:none;width:9px;height:12px;background:var(--orange);border-radius:2px 6px 2px 6px;margin-top:1px}
.regulation__photo{bottom:0;height:300px;background:linear-gradient(180deg,rgba(255,255,255,0) 0%,#e8e4df 35%,#c9c1b8 100%)}

/* outside spread – panel 1 */
.about__photo{top:0;height:250px;background:linear-gradient(180deg,#c9ccd1 0%,#dfe1e4 60%,#ffffff 100%)}
.about{position:absolute;top:262px;left:38px;right:40px}
.about p{font-size:10px;line-height:1.28;margin-top:12px}
.about .section-title{font-size:14px}
.cards{display:flex;flex-direction:column;gap:18px;margin-top:22px}
.card{display:flex;align-items:center;gap:20px;background:var(--grey-card);padding:10px 14px;border-radius:0 0 30px 0;font-size:10.5px;font-weight:500;line-height:1.25;min-height:76px}

/* outside spread – panel 2 */
.contact{position:absolute;inset:0;display:flex;flex-direction:column;align-items:center}
.badge{margin-top:226px;width:120px;height:120px;border-radius:50%;background:var(--white);display:flex;align-items:center;justify-content:center;text-align:center;padding:14px;font-size:11px;font-weight:700;color:var(--orange);line-height:1.25;box-shadow:0 2px 8px rgba(0,0,0,.2)}
.contact__title{margin-top:40px;font-size:22px;font-weight:800;color:var(--ink);text-transform:uppercase}
.contact__rule{width:250px;height:1px;background:rgba(255,255,255,.8);margin-top:12px}
.contact__list{list-style:none;align-self:flex-start;margin:26px 0 0 74px;display:flex;flex-direction:column;gap:16px}
.contact__list li{display:flex;gap:12px;align-items:flex-start;font-size:10px;font-weight:600}
.contact__list svg{flex:none;width:14px;height:14px;margin-top:1px}
.contact__list .phone{font-size:22px;font-weight:800;align-items:center}
.contact__list .phone svg{width:18px;height:18px;margin-top:0}
.addr strong{display:block;font-size:12px;font-weight:700;text-transform:uppercase}
.addr span{display:block;font-weight:400;margin-top:3px;line-height:1.3}
.social{margin-top:28px;display:flex;border:2px solid var(--ink);width:158px;height:30px}
.social span{flex:1;display:flex;align-items:center;justify-content:center}
.social span::before{content:"";width:12px;height:12px;background:var(--ink);border-radius:2px}

/* outside spread – panel 3 */
.cover__badge{position:absolute;top:16px;left:50%;transform:translateX(-50%);width:132px;height:132px;border-radius:50%;background:var(--white);border:2px solid #ddd;display:flex;align-items:center;justify-content:center;text-align:center;padding:16px;font-size:12px;font-weight:700;color:var(--orange);line-height:1.25;z-index:2}
.cover__photo{top:96px;height:448px;background:linear-gradient(160deg,#aab7c2 0%,#8f8a82 45%,#5e5a57 100%)}
.cover__title{position:absolute;top:570px;left:0;right:0;text-align:center}
.cover__title .l1,.cover__title .l2{font-size:27px;line-height:1.1;color:var(--ink);text-transform:uppercase}
.cover__title .l1{font-weight:500}
.cover__title .l2{font-weight:800}
.cover__title .l3{font-family:"Oswald",sans-serif;font-weight:600;font-size:48px;line-height:1.05;color:var(--orange);text-transform:uppercase}
.cover__bar{width:50px;height:4px;background:var(--ink);margin:12px auto 0}
.cover__strip{position:absolute;top:780px;left:0;right:0;height:26px;background:var(--orange);color:var(--white);font-size:10.5px;display:flex;align-items:center;justify-content:center;gap:8px}
.cover__strip b{font-family:Georgia,serif;font-size:16px}
.cover__web{position:absolute;top:822px;left:0;right:0;text-align:center;font-size:10px}
</style>
</head>
<body>

<!-- Inside spread -->
<section class="spread spread--inside">
  <div class="panel">
    <div class="photo industry__photo" role="img" aria-label="Photo of a business handshake over a desk"></div>
    <div class="photo industry__chess" role="img" aria-label="Photo of chess pieces lined up on a board"></div>
    <div class="industry__body">
      <h2 class="section-title">About our <em>industry</em></h2>
      <div class="rule"></div>
      <div class="industry__list">
        <div class="icon-row"><span class="icon-tile"><svg viewBox="0 0 26 26" fill="none" stroke="#fff" stroke-width="2"><rect x="6" y="3" width="14" height="20" rx="2"/><line x1="10" y1="9" x2="16" y2="9"/></svg></span><p>Pawnbroking is the oldest form of regulated consumer credit.</p></div>
        <div class="icon-row"><span class="icon-tile"><svg viewBox="0 0 26 26" fill="none" stroke="#fff" stroke-width="2"><rect x="5" y="3" width="14" height="19" rx="1"/><line x1="8" y1="8" x2="16" y2="8"/><line x1="8" y1="12" x2="16" y2="12"/><circle cx="19" cy="19" r="4"/></svg></span><p>The Department of Consumer and Business Services issues the pawnbroker licenses here in Oregon.</p></div>
        <div class="icon-row"><span class="icon-tile"><svg viewBox="0 0 26 26" fill="none" stroke="#fff" stroke-width="2"><path d="M3 5h4l3 11h11l2-8H8"/><circle cx="11" cy="20" r="1.5"/><circle cx="19" cy="20" r="1.5"/></svg></span><p>Currently, Oregon has 83 individually licensed pawnshops, 78 of which are brick-and-mortar, family-owned and operated businesses.</p></div>
        <div class="icon-row"><span class="icon-tile"><svg viewBox="0 0 26 26" fill="none" stroke="#fff" stroke-width="2"><circle cx="14" cy="9" r="6"/><path d="M3 20h6l4 2h8"/></svg></span><p>Pawnbrokers offer highly regulated safety-net funds to consumers on a face-to-face basis from Main Street locations across the state.</p></div>
        <div class="icon-row"><span class="icon-tile"><svg viewBox="0 0 26 26" fill="none" stroke="#fff" stroke-width="2"><path d="M13 4l4 7H9z"/><path d="M5 20l4-7 4 7z"/><path d="M15 20l4-7 4 7z"/></svg></span><p>Lending decisions are solely based on the collateral and pawn transactions are non-recourse. No credit inquiries, No credit reporting, No collections, No cycle of debt.</p></div>
        <div class="icon-row"><span class="icon-tile"><svg viewBox="0 0 26 26" fill="none" stroke="#fff" stroke-width="2"><path d="M3 10l10-6 10 6v12H3z"/><rect x="7" y="13" width="12" height="6"/></svg></span><p>Pawnbrokers provide safe, secure storage for items customers cannot or do not want to store themselves, including oversized or seasonal items construction equipment, and firearms.</p></div>
      </div>
    </div>
  </div>

  <div class="panel panel--orange">
    <div class="why">
      <h2 class="section-title"><span class="dark">Why pawnbrokers are</span> important<br>to Oregon consumers?</h2>
      <div class="rule"></div>
      <ul class="bullets">
        <li><span class="dot"></span>Without state-licensed pawnbrokers, Oregonians could be forced to borrow from unlicensed people with unregulated loans that include very high interest rates or instead, forced to sell their property entirely, diminishing their personal assets.</li>
        <li><span class="dot"></span>Other credit based lenders, such as banks and credit unions, do not offer Oregonians loan products at the small dollar amounts our industry serves.</li>
        <li><span class="dot"></span>Pawnbrokers provide a same day financial solution.</li>
        <li><span class="dot"></span>Pawnbrokers are invested in our communities and are sensitive to the needs of our customers.</li>
      </ul>
      <div class="stats">
        <h2 class="section-title">Oregon pawnbroker statistics<br>(as reported by DCBS)</h2>
        <div class="rule"></div>
        <ul class="stats__list">
          <li><span class="dollar">$</span>Average loan amount in 2020 was $175</li>
          <li><span class="dollar">$</span>Redemption rate of 72%</li>
          <li><span class="dollar">$</span>Oregon pawnshops made approximately 206,500 loans in 2020, lending $33.2 million to Oregon customers.</li>
          <li><span class="dollar">$</span>Police pickup rate of 0.085%</li>
        </ul>
      </div>
    </div>
    <div class="why__art" role="img" aria-label="Illustration of a laptop with growth charts, light bulb, hourglass and gears"></div>
  </div>

  <div class="panel">
    <div class="photo regulation__photo" role="img" aria-label="Photo of cash being handed across a desk beside gold jewellery"></div>
    <div class="regulation">
      <h2 class="section-title">Regulation</h2>
      <div class="rule"></div>
      <ul class="reg__list">
        <li><span class="reg__icon"><span></span></span>Pawnshops are heavily regulated and work closely with the federal, state and local governments and law enforcement.</li>
        <li><span class="reg__icon"><span></span></span>ORS 726 and OAR 441-740 define the requirements for our industry here in Oregon including the requirements of a loan, duration of a loan, as well as the interest and fees charged.</li>
        <li><span class="reg__icon"><span></span></span>Transactions require customer to present government issued photo identification.</li>
        <li><span class="reg__icon"><span></span></span>All transactions are reported daily to law enforcement.</li>
        <li><span class="reg__icon"><span></span></span>Oregon Pawnbrokers work closely with the following regulators:</li>
      </ul>
      <ul class="agencies">
        <li><span class="mark"></span>Department of Consumer and<br>Business Services</li>
        <li><span class="mark"></span>Bureau of Alcohol Tobacco and<br>Firearms</li>
        <li><span class="mark"></span>State Police</li>
        <li><span class="mark"></span>Department of Agriculture</li>
      </ul>
    </div>
  </div>
</section>

<!-- Outside spread -->
<section class="spread spread--outside">
  <div class="panel">
    <div class="photo about__photo" role="img" aria-label="Photo of a smiling business team standing together"></div>
    <div class="about">
      <h2 class="section-title">About <em>us</em></h2>
      <div class="rule"></div>
      <p>The Willamette Pawnbrokers Guild was officially established in 1989 by a forward thinking group of pawnbrokers who wanted to promote positive change to Oregon's pawn industry. Today, the Guild is the driving force behind many of these necessary changes while keeping a watchful eye on proposed government change that could adversely impact our industry.</p>
      <p>Our association strives to sustain the highest level of ethical conduct by adhering to established best practices and conforming to federal, state and local laws and regulation. Our members strive to be respected by their communities fostering strong relationships with law enforcement, state legislators, local government and community leaders.</p>
      <h2 class="section-title" style="margin-top:18px">About the Willamette<br><em>Pawnbrokers Guild</em></h2>
      <div class="rule"></div>
      <div class="cards">
        <div class="card"><span class="icon-tile"><svg viewBox="0 0 26 26" fill="none" stroke="#fff" stroke-width="2"><path d="M3 12l10-8 10 8"/><rect x="6" y="11" width="14" height="11"/><circle cx="13" cy="16" r="2"/></svg></span>United voice of Oregon Pawnbrokers.</div>
        <div class="card"><span class="icon-tile"><svg viewBox="0 0 26 26" fill="none" stroke="#fff" stroke-width="2"><rect x="5" y="3" width="14" height="19" rx="1"/><line x1="8" y1="8" x2="16" y2="8"/><line x1="8" y1="12" x2="16" y2="12"/><circle cx="19" cy="19" r="4"/></svg></span>Represents majority of pawn brokers, both number of licenses and transactions processed.</div>
        <div class="card"><span class="icon-tile"><svg viewBox="0 0 26 26" fill="none" stroke="#fff" stroke-width="2"><rect x="5" y="3" width="16" height="20" rx="2"/><circle cx="13" cy="13" r="4"/></svg></span>Single point of contact for Oregon Legislature and all regulators to communicate with our industry.</div>
      </div>
    </div>
  </div>

  <div class="panel panel--orange">
    <div class="contact">
      <div class="badge">Willamette Pawnbrokers Guild</div>
      <h2 class="contact__title">Contact us</h2>
      <div class="contact__rule"></div>
      <ul class="contact__list">
        <li class="phone"><svg viewBox="0 0 18 18" fill="var(--ink)"><path d="M2 7c0-3 3-5 7-5s7 2 7 5h-4V5H6v2zM4 9h10l1 7H3z"/></svg>+123 456 7890</li>
        <li class="addr"><svg viewBox="0 0 14 14" fill="var(--ink)"><path d="M7 1a4 4 0 0 1 4 4c0 3-4 8-4 8S3 8 3 5a4 4 0 0 1 4-4z"/></svg><div><strong>Lorem Ipsum</strong><span>Lorem ipsum, Lorem city,<br>Lorem State, Lorem 986453</span></div></li>
        <li><svg viewBox="0 0 14 14" fill="none" stroke="var(--ink)" stroke-width="1.3"><circle cx="7" cy="7" r="6"/><line x1="1" y1="7" x2="13" y2="7"/><ellipse cx="7" cy="7" rx="2.5" ry="6"/></svg>www.willamettepawnguild.com</li>
        <li><svg viewBox="0 0 14 14" fill="none" stroke="var(--ink)" stroke-width="1.3"><rect x="1" y="3" width="12" height="8"/><path d="M1 3l6 5 6-5"/></svg>Info@yourwebsitename.com</li>
      </ul>
      <div class="social"><span></span><span></span><span></span></div>
    </div>
  </div>

  <div class="panel">
    <div class="photo cover__photo" role="img" aria-label="Photo of business colleagues discussing around a laptop in an office"></div>
    <div class="cover__badge">Willamette Pawnbrokers Guild</div>
    <div class="cover__title">
      <div class="l1">Lending solution</div>
      <div class="l2">For your total</div>
      <div class="l3">Money needs</div>
      <div class="cover__bar"></div>
    </div>
    <div class="cover__strip"><b>“</b>The oldest form of regulated consumer credit<b>”</b></div>
    <div class="cover__web">www.willamettepawnguild.com</div>
  </div>
</section>

</body>
</html>
```